brochure for high-end senior living company

We need a new brochure that we can pass out to doctors and social workers so they would choose us over the competition.
quietharborgrove.com is our website that shows our colors and themes

we stand out over our competition due to our high quality of staff and our staff to resident ratio.
We are not afraid of difficult and complex care situations. Instead, we thrive on coordinating complexity.

We do all of this in a lovely setting that is luxurious and feels like home.

Target Market(s)

The families who make the decision are 60-70 years old. They are not not "rich" but they have saved well and usually have more than 1 million in assets.

Industry/Entity Type

Senior Living, Memory Care

Font styles to use
Serif

Colors
00AB8E
00BBA5
67D7C9
C6EFE9
E9F9F6
FFC000
F8CF3A
FAE287
FDF2CF
FEFAEE

Requirements
Must have
• When compromise is not an option...
Nice to have
• A difficult balance of beautiful and activities (happy people), but also communicating that we handle difficult and complex care.

```html
<!DOCTYPE html>
<html lang="en">
<head>
<meta charset="utf-8">
<title>Quiet Harbor Grove Brochure</title>
<link href="https://fonts.googleapis.com/css2?family=Roboto:wght@400;500;700;900&display=swap" rel="stylesheet">
<style>
:root{
  --forest:#083f3a;
  --forest-deep:#0b3330;
  --gold:#d9a90f;
  --gold-text:#c99a0a;
  --ink:#1c1c1c;
  --body:#5a5a5a;
  --paper:#ffffff;
  --mist:#f3f3f3;
  --teal:#67d7c9;
}
*{margin:0;padding:0;box-sizing:border-box}
html,body{width:891px;height:1200px;overflow:hidden;background:var(--paper)}
body{position:relative;font-family:"Roboto",sans-serif;color:var(--ink)}
.page{position:absolute;width:363px;height:516px;background:var(--paper);box-shadow:0 0 6px rgba(0,0,0,.08);overflow:hidden}
.page--cover{left:46px;top:47px}
.page--about{left:458px;top:47px}
.page--testimonials{left:46px;top:630px;background:linear-gradient(180deg,#fbfbfb,#f1efe9)}
.page--grounds{left:458px;top:630px}
.abs{position:absolute}
.photo{position:absolute}
.frame{position:absolute;background:var(--paper);box-shadow:0 1px 5px rgba(0,0,0,.15)}

/* cover */
.cover-band{left:0;top:0;width:363px;height:259px;background:var(--forest)}
.brand-name{left:0;top:24px;width:363px;text-align:center;color:#fff;font-weight:500;font-size:15px;letter-spacing:.06em}
.cover-frame{left:31px;top:75px;width:301px;height:312px}
.cover-photo{left:3px;top:3px;right:3px;bottom:3px;background:radial-gradient(circle at 65% 30%,#e6d5c8 0,#9aa6a4 45%,#4a5560 100%)}
.vertical{writing-mode:vertical-rl;transform:rotate(180deg);white-space:nowrap;font-weight:900;line-height:1}
.headline-small{left:51px;bottom:28px;font-size:17px;font-weight:700;color:var(--ink)}
.headline-big{left:70px;bottom:27px;font-size:28px;color:var(--ink)}
.cover-copy{left:138px;top:400px;width:194px;font-size:4.6px;line-height:9.1px;color:var(--body)}
.cover-tagline{right:32px;top:481px;font-size:4.5px;font-weight:700;letter-spacing:.08em;color:var(--gold-text)}

/* about */
.about-col{left:31px;top:32px;width:143px}
.about-heading{font-size:11.2px;font-weight:700;color:var(--ink);margin-bottom:5px;white-space:nowrap}
.about-text{font-size:4.9px;line-height:9.1px;color:var(--body);margin-bottom:17px}
.about-mesh{left:0;top:370px;width:363px;height:146px;background:linear-gradient(180deg,rgba(255,255,255,0),#ececec 60%,#f6f6f6)}
.about-frame{left:186px;top:35px;width:146px;height:410px}
.about-photo{left:3px;top:3px;right:3px;bottom:3px;background:linear-gradient(160deg,#c6efe9 0,#67d7c9 45%,#2f8f86 100%)}
.about-label{left:31px;top:479px;font-size:25px;font-weight:900;color:rgba(200,200,200,.75)}

/* testimonials */
.test-yellow{left:81px;top:126px;width:282px;height:339px;background:var(--gold)}
.test-frame{left:0;top:0;width:256px;height:278px}
.test-photo{left:5px;top:6px;right:6px;bottom:6px;background:linear-gradient(150deg,#d8d1c4 0,#a9574b 40%,#2f3a3c 100%)}
.test-label{left:21px;bottom:10px;font-size:27px;color:var(--ink)}
.test-heading{left:113px;top:310px;width:230px;font-size:11.5px;font-weight:700;line-height:18.5px;color:var(--forest)}
.quote-mark{left:112px;top:355px;width:22px;height:20px}
.quote-text{left:113px;top:387px;width:200px;font-size:4.7px;line-height:9.5px;color:#fff}
.quote-name{left:113px;top:418px;font-size:7.6px;font-weight:700;color:#fff}

/* grounds */
.grounds-photo{left:0;top:0;width:363px;height:516px;background:linear-gradient(180deg,#5d8fc4 0,#3e5f3a 38%,#c9c9c2 60%,#9da53a 72%,#0f3b36 86%,var(--forest-deep) 100%)}
.grounds-copy{left:31px;top:342px;width:320px;font-size:17.6px;font-weight:700;line-height:29.4px;color:#fff;text-transform:uppercase}
</style>
</head>
<body>

<section class="page page--cover">
  <div class="abs cover-band"></div>
  <div class="abs brand-name">Quiet Harbor Grove</div>
  <div class="frame cover-frame">
    <div class="photo cover-photo" role="img" aria-label="Smiling senior woman holding a caregiver's hand"></div>
  </div>
  <div class="abs vertical headline-small">WHEN COMPROMISE</div>
  <div class="abs vertical headline-big">IS NOT AN OPTION.</div>
  <p class="abs cover-copy">Quiet Harbor Grove, our team of highly trained and caring professionals provides a welcoming and comfortable assisted living environment for our residents to enjoy for many years to come. Unlike other communities, our Maplecrest assisted living home is located in a residential setting because we believe it brings a greater value to our residents as they maintain feelings of safety, warmth, and familiarity. The most beneficial factor of living in our community is the great amount of personal care and attention we are able to give each one of our residents. In fact, we maintain the highest caregiver to resident ratio in the assisted living industry.</p>
  <div class="abs cover-tagline">AROUND THE CLOCK QUALITY CARE FOR YOUR LOVED ONE.</div>
</section>

<section class="page page--about">
  <div class="abs about-mesh" role="img" aria-label="Soft grey geometric mesh background"></div>
  <div class="abs about-col">
    <h2 class="about-heading">WHAT WE DO</h2>
    <p class="about-text">In America, people aren't used to assistance. We love independence and freedom and don't plan on giving them up. At Quiet Harbor Grove, we get that. When a person comes through our doors and needs to transition to more assistance, we work very hard to make it painless and, dare we say, enjoyable! We come alongside strong independent people and offer gentle, patient, and friendly help.</p>
    <h2 class="about-heading">WHY WE DO WHAT WE DO</h2>
    <p class="about-text">Being in assisted living such a long time, we saw the spectrum of care that exists out there. We saw a need for higher acuity care. So we set out to find the sweet balance of high quality care combined with a home atmosphere. We do that through a three-pronged method. First, we partner with licensed medical help every step of the way. Second, we hire CNAs, medical assistants, and nurses on their way to becoming registered. Third, we only choose homes that are spacious and inviting. We believe this balance accomplishes our pursuit of doing for our residents what we would like done for us.</p>
    <h2 class="about-heading">WHY WE'RE RESIDENTIAL</h2>
    <p class="about-text">The residential assisted living model allows us to keep the caregiver to resident ratio small. Simply put, the more residents, the more the caregivers are spread thin. In our environment we can achieve what we believe is the ideal ratio. We are also able to get to know every resident very closely. This is great relationally, but it's also medically advantages since we are able to quickly assess a change in medical condition.</p>
  </div>
  <div class="frame about-frame">
    <div class="photo about-photo" role="img" aria-label="Caregiver helping a senior resident with a walker, teal tinted"></div>
  </div>
  <div class="abs about-label">ABOUT US</div>
</section>

<section class="page page--testimonials">
  <div class="abs test-yellow"></div>
  <div class="frame test-frame">
    <div class="photo test-photo" role="img" aria-label="Resident and caregivers celebrating a birthday with party props"></div>
  </div>
  <div class="abs vertical test-label">TESTIMONIALS</div>
  <h2 class="abs test-heading">THE TEAM YOU NEED TO HELP YOU AND YOUR FAMILY</h2>
  <svg class="abs quote-mark" viewBox="0 0 22 20" aria-hidden="true">
    <path d="M0 20V11C0 5 3 1 9 0v3C6 4 5 6 5 9h4v11zM12 20V11c0-6 3-10 9-11v3c-3 1-4 3-4 6h4v11z" fill="#fff"/>
  </svg>
  <p class="abs quote-text">"I could not have chosen a more PERFECT home for my Mom to have spent the last year of her life in. She was happy and so well cared for. Never did I worry that she would be lonely or not attended to. ..."</p>
  <div class="abs quote-name">DIANE WHITFORD</div>
</section>

<section class="page page--grounds">
  <div class="photo grounds-photo" role="img" aria-label="Sunny garden path under oak trees leading to a residential home"></div>
  <p class="abs grounds-copy">A difficult balance of beauty and activities (happy people), but also communicating that we handle difficult and complex care</p>
</section>

</body>
</html>
```